Pop-up Banner

Would like a design for a pop-up 85 x 206cm banner for a trade show. (from norla press)
We would like "our logo" (brightwave holdings) - then the tagline - "Your Trusted Partner in Data-Driven Decisions"
*Supporting Bullets*
Unified data, analytics & AI
Trusted insights, faster outcomes
Real-time intelligence at scale
Enterprise-ready, secure solutions
Clarity from data complexity
trusted by...some company logos
Partners with : partner logo
Our Colours: #FFA300, #3D4176, #FDD16E, #F87C57, #A68118, #1C2F36

```html
<!DOCTYPE html>
<html lang="en">
<head>
<meta charset="utf-8">
<title>Brightwave Holdings – Pop-up Banner</title>
<link rel="stylesheet" href="https://fonts.googleapis.com/css2?family=Bebas+Neue&family=Poppins:wght@600;700&display=swap">
<style>
  :root {
    --orange: #FFA300;
    --orange-soft: #FDD16E;
    --navy: #3D4176;
    --ink: #1C2F36;
    --paper: #ffffff;
    --backdrop: #d6d6d6;
    --tile-border: #e3e5e8;
  }
  * { margin: 0; padding: 0; box-sizing: border-box; }
  html, body { width: 1200px; height: 1200px; overflow: hidden; }
  body { background: var(--backdrop); position: relative; font-family: "Poppins", sans-serif; }

  .banner {
    position: absolute; left: 365px; top: 30px;
    width: 470px; height: 1140px;
    background: radial-gradient(ellipse at 50% 55%, #ffffff 40%, #f1f2f4 100%);
    overflow: hidden;
  }
  .banner-shapes { position: absolute; inset: 0; }

  .brand {
    position: absolute; top: 30px; left: 0; width: 100%;
    display: flex; align-items: center; justify-content: center; gap: 16px;
  }
  .brand-dot { width: 62px; height: 62px; border-radius: 50%; background: var(--orange); }
  .brand-name {
    color: var(--orange); font-weight: 700; font-size: 27px; line-height: 1.08;
    letter-spacing: 1px; text-transform: uppercase;
  }

  .tagline { position: absolute; top: 218px; width: 100%; text-align: center; font-family: "Bebas Neue", sans-serif; }
  .tagline-lead { display: block; color: var(--ink); font-size: 45px; line-height: 50px; }
  .tagline-main { display: block; color: var(--navy); font-size: 59px; line-height: 60px; }

  .benefits { position: absolute; top: 364px; left: 0; width: 100%; list-style: none; }
  .benefit {
    height: 51px; margin: 0 auto 10px; border-radius: 26px;
    background: var(--orange); color: var(--ink);
    font-weight: 600; font-size: 19px;
    display: flex; align-items: center; justify-content: center; gap: 9px;
  }
  .benefit::before {
    content: ""; border-left: 8px solid var(--ink);
    border-top: 5px solid transparent; border-bottom: 5px solid transparent;
  }

  .section-label {
    position: absolute; left: 50%; transform: translateX(-50%);
    height: 35px; background: var(--ink); color: #fff;
    font-family: "Bebas Neue", sans-serif; font-size: 32px; line-height: 37px; text-align: center;
    clip-path: polygon(0 0, 100% 0, 94% 50%, 100% 100%, 0 100%, 6% 50%);
  }
  .section-label::before, .section-label::after { content: ""; }
  .label-trusted { top: 735px; width: 160px; }
  .label-partners { top: 881px; width: 200px; }

  .logo-row { position: absolute; left: 0; width: 100%; display: flex; justify-content: center; gap: 21px; }
  .row-clients { top: 798px; }
  .row-partners { top: 942px; }
  .logo-tile {
    width: 88px; height: 42px; background: #fff;
    border: 1px solid var(--tile-border); border-radius: 3px;
    box-shadow: 0 1px 3px rgba(0,0,0,0.08);
    display: flex; align-items: center; justify-content: center;
    color: var(--ink); font-weight: 600; font-size: 11.5px;
  }

  .website {
    position: absolute; top: 1078px; width: 100%; text-align: center;
    color: #fff; font-weight: 700; font-size: 25px;
  }
</style>
</head>
<body>
  <main class="banner">
    <svg class="banner-shapes" viewBox="0 0 470 1140" width="470" height="1140" aria-hidden="true">
      <path d="M0 0H470V190Q235 118 0 190Z" fill="var(--orange)"/>
      <path d="M0 0H470V170Q235 102 0 170Z" fill="var(--ink)"/>
      <path d="M0 182Q235 108 470 182" fill="none" stroke="#fff" stroke-width="3"/>
      <path d="M0 1000Q235 1080 470 1000V1140H0Z" fill="var(--orange)"/>
      <path d="M0 1022Q235 1092 470 1022V1140H0Z" fill="var(--ink)"/>
    </svg>

    <header class="brand">
      <span class="brand-dot"></span>
      <span class="brand-name">Brightwave<br>Holdings</span>
    </header>

    <h1 class="tagline">
      <span class="tagline-lead">Your Trusted Partner In</span>
      <span class="tagline-main">Data-Driven Decisions</span>
    </h1>

    <ul class="benefits">
      <li class="benefit" style="width:368px">Unified data, analytics &amp; AI</li>
      <li class="benefit" style="width:422px">Trusted insights, faster outcomes</li>
      <li class="benefit" style="width:397px">Real-time intelligence at scale</li>
      <li class="benefit" style="width:432px">Enterprise-ready, secure solutions</li>
      <li class="benefit" style="width:379px">Clarity from data complexity</li>
    </ul>

    <h2 class="section-label label-trusted">Trusted By</h2>
    <div class="logo-row row-clients">
      <span class="logo-tile">Crestline</span>
      <span class="logo-tile">Fernway</span>
      <span class="logo-tile">Lumora</span>
      <span class="logo-tile">Ostrava</span>
    </div>

    <h2 class="section-label label-partners">Partners With</h2>
    <div class="logo-row row-partners">
      <span class="logo-tile">Kestrel</span>
      <span class="logo-tile">Northmere</span>
      <span class="logo-tile">Halvane</span>
      <span class="logo-tile">Quillbridge</span>
    </div>

    <p class="website">www.brightwaveholdings.com</p>
  </main>
</body>
</html>
```